'Bright Ledger Keys Unlocked' Book Cover

I need a professional book cover design for my new upcoming book that shows people how to get a high credit score.

Here are my two websites:

https://www.moneywise-glossaro.info
https://moneywise-glossaro.com/

I am looking for a clean, professional design that pops (emotional touch) and separates from the other books that are on the market. Cover aspect ratio 1:4 for Pagewisp version and 1:5 for the paperback version. Yellow or blue are good colors - but not must. See the basic examples that I provided. File delivery format PDF.

Book Title: Bright Ledger Keys Unlocked
Byline: The Quick Lift And Mend Path to Stellar Standing

Currently on Parcelora pre-order:
https://www.parcelora.example/Bright-Ledger-Keys-Unlocked-Stellar-ebook/dp/Q93MPLLR7W

I am the author of 36 published books on Parcelora. My author profile is here:
parcelora.example/author/wendelbrisk

Targeted audience: People that want to improve or repair their bad credit score.

Target Market(s)

People/consumers in the US that want to improve or repair their credit score.

Industry/Entity Type

Consumer

Font styles to use
Sans Serif

Colors

Designer to choose colors to be used in the design.

Requirements
Must have
• Author name, Title, byline, and graphic element(s).
Nice to have
• - 2020 edition logo / batch

```html
<!DOCTYPE html>
<html lang="en">
<head>
<meta charset="utf-8">
<title>Bright Ledger Keys Unlocked – Book Cover</title>
<link rel="stylesheet" href="https://fonts.googleapis.com/css2?family=Bebas+Neue&family=Libre+Baskerville&display=swap">
<style>
  :root {
    --page-bg: #f4f4f4;
    --cover-blue: #0a67b2;
    --cover-blue-light: #1b78c0;
    --cover-yellow: #d6d405;
    --author-yellow: #d8d800;
    --title-white: #ffffff;
    --subtitle-ink: #111111;
    --photo-red: #d81e22;
    --photo-red-dark: #b8161a;
    --photo-hair: #3a1c14;
    --photo-skin: #8a4a36;
  }
  * { margin: 0; padding: 0; box-sizing: border-box; }
  html, body {
    width: 1200px;
    height: 800px;
    overflow: hidden;
    background: var(--page-bg);
  }
  .canvas {
    position: relative;
    width: 1200px;
    height: 800px;
    display: flex;
    align-items: center;
    justify-content: center;
  }
  .cover {
    position: relative;
    width: 440px;
    height: 720px;
    overflow: hidden;
    background: var(--cover-blue);
    box-shadow: 0 10px 30px rgba(0,0,0,0.18);
  }
  .cover__blue-panel {
    position: absolute;
    inset: 0 0 auto 0;
    height: 402px;
    background: linear-gradient(90deg, var(--cover-blue-light) 0%, var(--cover-blue) 12%, var(--cover-blue) 100%);
  }
  .cover__yellow-panel {
    position: absolute;
    left: 0; right: 0; bottom: 0;
    top: 402px;
    background: var(--cover-yellow);
  }
  .cover__author {
    position: absolute;
    top: 22px;
    left: 0; right: 0;
    text-align: center;
    font-family: 'Bebas Neue', sans-serif;
    font-size: 38px;
    line-height: 44px;
    letter-spacing: 3px;
    color: var(--author-yellow);
    z-index: 3;
  }
  .cover__title {
    position: absolute;
    top: 90px;
    left: 30px;
    right: 10px;
    font-family: 'Bebas Neue', sans-serif;
    font-weight: 400;
    font-size: 80px;
    line-height: 90px;
    color: var(--title-white);
    white-space: nowrap;
    z-index: 3;
  }
  .cover__title span { display: block; }
  .cover__photo {
    position: absolute;
    inset: 0;
    z-index: 2;
  }
  .cover__photo-head {
    position: absolute;
    left: 288px;
    right: 0;
    top: 215px;
    height: 280px;
    border-radius: 90px 0 0 0;
    background: linear-gradient(180deg, var(--photo-hair) 0%, #5a2e22 45%, var(--photo-skin) 100%);
  }
  .cover__photo-body {
    position: absolute;
    left: 222px;
    right: 0;
    top: 470px;
    bottom: 0;
    border-radius: 40px 0 0 0;
    background: linear-gradient(180deg, var(--photo-red) 0%, var(--photo-red-dark) 100%);
  }
  .cover__subtitle {
    position: absolute;
    top: 448px;
    left: 56px;
    width: 160px;
    font-family: 'Libre Baskerville', serif;
    font-size: 20px;
    line-height: 31px;
    text-transform: uppercase;
    color: var(--subtitle-ink);
    white-space: nowrap;
    z-index: 3;
  }
  .cover__subtitle span { display: block; }
</style>
</head>
<body>
  <main class="canvas">
    <section class="cover" aria-label="Book cover">
      <div class="cover__blue-panel"></div>
      <div class="cover__yellow-panel"></div>
      <div class="cover__photo" role="img" aria-label="Photo of a smiling young woman in a red sweater holding up a credit card">
        <div class="cover__photo-head"></div>
        <div class="cover__photo-body"></div>
      </div>
      <p class="cover__author">Wendel Brisk</p>
      <h1 class="cover__title">
        <span>Bright Ledger</span>
        <span>Keys</span>
        <span>Unlocked</span>
      </h1>
      <p class="cover__subtitle">
        <span>The Quick</span>
        <span>Lift And</span>
        <span>Mend</span>
        <span>Path to</span>
        <span>Stellar</span>
        <span>Standing</span>
      </p>
    </section>
  </main>
</body>
</html>
```